Innovative Bitcoin Powerpoint Presentation

I have constructred most of the data for a 15 page powerpoint presentation on an innovative bitcoin idea that provides access to fiat currency with bitcoin hodlings

I need this to look great as a first blush to potential investors

Reason: updated deck and name

Target Market(s)

Venture Capital firms and private equity firms

Requirements
Must have
• Fun, innovateive deck, very clean
Should not have
• any generic feel - no templates

```html
<!DOCTYPE html>
<html lang="en">
<head>
<meta charset="utf-8">
<title>Trailcoin Investor Deck – Slide Overview</title>
<link rel="stylesheet" href="https://fonts.googleapis.com/css2?family=Fjalla+One&family=Roboto+Condensed:wght@300;400;700&display=swap">
<style>
  :root {
    --board: #000000;
    --blue-deep: #0d5da8;
    --blue-mid: #1a7fd0;
    --blue-light: #3a9be3;
    --white: #ffffff;
    --pale: #e9f0f6;
    --orange: #f7941d;
    --orange-box: #f9a14c;
    --box-blue: #2f78bd;
    --box-teal: #2bb598;
    --ink: #222222;
    --muted: #4a4a4a;
    --teal-text: #19a99a;
    --plum: #6a1a3d;
    --connector: #8c8c8c;
  }
  * { box-sizing: border-box; margin: 0; padding: 0; }
  html, body { width: 1200px; height: 918px; overflow: hidden; background: var(--board); }
  body { font-family: "Roboto Condensed", Arial, sans-serif; position: relative; }

  .slide { position: absolute; width: 563px; overflow: hidden; background: var(--white); }
  .slide--title   { left: 26px;  top: 25px;  height: 423px; }
  .slide--cover   { left: 610px; top: 25px;  height: 423px; }
  .slide--figures { left: 26px;  top: 469px; height: 422px; }
  .slide--points  { left: 610px; top: 469px; height: 422px; }

  .tech-field {
    position: absolute; left: 0; width: 100%;
    background: radial-gradient(ellipse at 45% 30%, var(--blue-light) 0%, var(--blue-mid) 40%, var(--blue-deep) 100%);
  }

  /* Title slide */
  .slide--title .tech-field--top { top: 0; height: 234px; }
  .slide--title .tech-field--bottom { top: 377px; height: 46px; }
  .title-band { position: absolute; left: 0; top: 234px; width: 100%; height: 143px; background: var(--white); }
  .wordmark {
    position: absolute; display: flex; align-items: center; gap: 8px;
    font-family: "Roboto Condensed", Arial, sans-serif; font-weight: 400; color: var(--plum);
  }
  .wordmark__dot { width: 22px; height: 22px; border-radius: 50%; background: var(--plum); }
  .title-band .wordmark { left: 140px; top: 52px; font-size: 30px; }
  .title-band__divider { position: absolute; left: 328px; top: 18px; width: 1px; height: 108px; background: #9a9a9a; }
  .title-band__project { position: absolute; left: 344px; top: 18px; font-family: "Fjalla One", sans-serif; font-size: 25px; color: var(--orange); }
  .title-band__author { position: absolute; left: 346px; top: 61px; font-size: 12px; color: var(--teal-text); }
  .title-band__subtext { position: absolute; left: 346px; top: 89px; width: 200px; font-size: 10.5px; line-height: 16px; color: var(--ink); }

  /* Cover slide */
  .slide--cover .tech-field--top { top: 0; height: 231px; }
  .cover-band { position: absolute; left: 0; top: 231px; width: 100%; height: 162px; background: var(--pale); }
  .cover-band .wordmark { left: 50%; top: 62px; transform: translateX(-50%); font-size: 32px; }
  .cover-rule { position: absolute; left: 0; top: 395px; width: 100%; height: 28px; background: var(--orange); border-top: 2px solid var(--white); box-shadow: 0 -2px 0 var(--orange); }

  /* Content slides */
  .slide-header { position: absolute; left: 0; top: 0; width: 100%; height: 60px; }
  .slide-header .tech-field { top: 0; height: 60px; }
  .slide-header__title { position: absolute; left: 22px; top: 12px; font-weight: 300; font-size: 29px; color: var(--white); }
  .slide-header .wordmark { right: 14px; top: 18px; font-size: 18px; color: var(--white); }
  .slide-footer {
    position: absolute; left: 0; top: 396px; width: 100%; height: 26px;
    background: var(--orange); border-top: 2px solid var(--white); box-shadow: 0 -2px 0 var(--orange);
  }
  .slide-footer__text { position: absolute; left: 6px; top: 5px; font-size: 11px; color: var(--white); }

  /* Figure cards */
  .stat { position: absolute; top: 149px; width: 123px; }
  .stat--blue   { left: 43px;  --accent: var(--box-blue); }
  .stat--orange { left: 227px; --accent: var(--orange-box); }
  .stat--teal   { left: 411px; --accent: var(--box-teal); }
  .stat__value {
    height: 62px; background: var(--accent); color: var(--white);
    font-weight: 300; font-size: 36px; line-height: 62px; text-align: center;
    box-shadow: 0 0 0 2px #f0f0f0;
  }
  .stat__link { width: 2px; height: 44px; margin: 0 auto; background: var(--connector); }
  .stat__label {
    height: 60px; border: 1.5px solid var(--accent); border-radius: 2px;
    font-weight: 300; font-size: 16px; line-height: 21px; color: var(--muted);
    text-align: center; padding-top: 8px;
  }

  /* Bullet points */
  .points { position: absolute; left: 31px; top: 88px; list-style: none; }
  .point { position: relative; padding-left: 23px; margin-bottom: 11px; }
  .point__tick { position: absolute; left: 0; top: 2px; width: 16px; height: 14px; }
  .point__heading { font-family: "Fjalla One", sans-serif; font-size: 15.5px; color: var(--orange); letter-spacing: 0.2px; }
  .point__detail { padding-left: 24px; margin-top: 4px; font-size: 12.5px; line-height: 21px; color: var(--ink); }
</style>
</head>
<body>

<!-- Title slide -->
<section class="slide slide--title">
  <div class="tech-field tech-field--top" role="img" aria-label="Blue circuit-board and binary digits background"></div>
  <div class="title-band">
    <div class="wordmark"><span class="wordmark__dot"></span>Trailcoin</div>
    <div class="title-band__divider"></div>
    <h1 class="title-band__project">Project Title Here</h1>
    <p class="title-band__author">Marcus Delaney</p>
    <p class="title-band__subtext">Subtext here Subtext here Subtext here Subtext here Subtext here Subtext here</p>
  </div>
  <div class="tech-field tech-field--bottom" role="img" aria-label="Blue circuit-board strip"></div>
</section>

<!-- Cover slide -->
<section class="slide slide--cover">
  <div class="tech-field tech-field--top" role="img" aria-label="Blue circuit-board and binary digits background"></div>
  <div class="cover-band">
    <div class="wordmark"><span class="wordmark__dot"></span>Trailcoin</div>
  </div>
  <div class="cover-rule"></div>
</section>

<!-- Figures slide -->
<section class="slide slide--figures">
  <header class="slide-header">
    <div class="tech-field" role="img" aria-label="Blue circuit-board header strip"></div>
    <h2 class="slide-header__title">Project Title Here</h2>
    <div class="wordmark">Trailcoin</div>
  </header>
  <div class="stat stat--blue">
    <div class="stat__value">13.5m</div><div class="stat__link"></div>
    <div class="stat__label">BTC IN<br>CIRCULATION</div>
  </div>
  <div class="stat stat--orange">
    <div class="stat__value">13.5m</div><div class="stat__link"></div>
    <div class="stat__label">BTC IN<br>CIRCULATION</div>
  </div>
  <div class="stat stat--teal">
    <div class="stat__value">13.5m</div><div class="stat__link"></div>
    <div class="stat__label">BTC IN<br>CIRCULATION</div>
  </div>
  <footer class="slide-footer"><span class="slide-footer__text">Copyright text here</span></footer>
</section>

<!-- Key points slide -->
<section class="slide slide--points">
  <header class="slide-header">
    <div class="tech-field" role="img" aria-label="Blue circuit-board header strip"></div>
    <h2 class="slide-header__title">Project Title Here</h2>
    <div class="wordmark">Trailcoin</div>
  </header>
  <ul class="points">
    <li class="point">
      <svg class="point__tick" viewBox="0 0 16 14"><path d="M1 8 L6 12 L15 1" fill="none" stroke="#f7941d" stroke-width="2.6" stroke-linecap="round" stroke-linejoin="round"/></svg>
      <div class="point__heading">Secured line of credit leveraging BTC collateral</div>
      <div class="point__detail">Reduces BTC currency exchange costs<br>Mitigates price volatility risk</div>
    </li>
    <li class="point">
      <svg class="point__tick" viewBox="0 0 16 14"><path d="M1 8 L6 12 L15 1" fill="none" stroke="#f7941d" stroke-width="2.6" stroke-linecap="round" stroke-linejoin="round"/></svg>
      <div class="point__heading">$300m credit facility secured</div>
      <div class="point__detail">Provided by one of the worlds largest P/E firms</div>
    </li>
    <li class="point">
      <svg class="point__tick" viewBox="0 0 16 14"><path d="M1 8 L6 12 L15 1" fill="none" stroke="#f7941d" stroke-width="2.6" stroke-linecap="round" stroke-linejoin="round"/></svg>
      <div class="point__heading">Global opportunity</div>
    </li>
    <li class="point">
      <svg class="point__tick" viewBox="0 0 16 14"><path d="M1 8 L6 12 L15 1" fill="none" stroke="#f7941d" stroke-width="2.6" stroke-linecap="round" stroke-linejoin="round"/></svg>
      <div class="point__heading">Scalable API integration</div>
    </li>
    <li class="point">
      <svg class="point__tick" viewBox="0 0 16 14"><path d="M1 8 L6 12 L15 1" fill="none" stroke="#f7941d" stroke-width="2.6" stroke-linecap="round" stroke-linejoin="round"/></svg>
      <div class="point__heading">First to market advantage</div>
    </li>
  </ul>
  <footer class="slide-footer"><span class="slide-footer__text">Copyright text here</span></footer>
</section>

</body>
</html>
```